Poster for a Bicycle show/Expo

We need a poster for a Bicycle show/Expo and sustainable transport. Exhibitors will sell bikes, cycling clothing, accessories, etc. ...
This show is annual and the Poster is for the 2016 edition.

Your concept must be compatible in a landscape format. (We will ourselves adaptations of different formats.)
Width: 210 mm
Height: 297 mm
It's necessary for us to have the source file (vector) for make, later, the different format (flyers, website, ...)

Content of the Poster:
- 1 big picture (one of the two attached)
- Big title (typo-title worked): « Foire du Rouet » (« Salon » or « Salon du » can be small and « Vélo » big.)
- Subtitle: « et de la mobilité durable »
- Date: « 18, 19 et 20 mars 2016 » or « 18-20 mars 2016 »
- Place: « Halle RTP - Gare de Plantaz »
- Text line 1: « www.foire-du-rouet.ch »
- Text line 2: « Entrée gratuite »
- Text line 3: « Ve 18 mars de 17h à 20h - Sa 19 mars de 10h à 18h - Di 20 mars de 10h à 17h »
- Please, leave a zone in the poster for sponsors logos
(The predominant information (most visible) are: « Vélo » and « 18, 19 et 20 mars 2016 » or « 18-20 mars 2016 »)

Target Market(s)

Bicycle fan

Industry/Entity Type

Sporting Good

Font styles to use
Serif
Sans Serif

Colors
add136
ffffff
ec1f27

Requirements
Must have
• The style must be modern, dynamic, bright colors.

```html
<!DOCTYPE html>
<html lang="fr">
<head>
<meta charset="utf-8">
<title>Foire du Rouet 2016 – Affiche</title>
<link rel="stylesheet" href="https://fonts.googleapis.com/css2?family=Open+Sans:wght@400;600;700&display=swap">
<style>
  :root {
    --sky-deep: #1b4a94;
    --sky-mid: #3f78c2;
    --sky-light: #8fb6e2;
    --sky-pale: #d6e5f4;
    --paper: #ffffff;
    --ink: #1e2a45;
    --cloud: #f4f8fd;
    --cloud-edge: #c9dcf1;
  }
  * { margin: 0; padding: 0; box-sizing: border-box; }
  html, body { width: 849px; height: 1200px; overflow: hidden; background: var(--paper); }
  .poster {
    position: relative;
    width: 849px;
    height: 1200px;
    overflow: hidden;
    font-family: "Open Sans", Arial, sans-serif;
    color: var(--ink);
    background: linear-gradient(180deg,
      var(--sky-deep) 0%,
      var(--sky-mid) 38%,
      var(--sky-light) 60%,
      var(--sky-pale) 68%,
      var(--paper) 74%,
      var(--paper) 100%);
  }
  .title {
    position: absolute;
    left: 212px; top: 70px;
    color: var(--paper);
    font-weight: 600;
  }
  .title-small {
    display: block;
    font-size: 44px;
    line-height: 1;
  }
  .title-big {
    display: block;
    font-size: 132px;
    line-height: 1;
    letter-spacing: -2px;
    margin-top: -4px;
    margin-left: 110px;
  }
  .subtitle {
    display: block;
    font-size: 28px;
    font-weight: 400;
    margin-top: 4px;
    margin-left: 128px;
  }
  .hero-visual {
    position: absolute;
    left: 141px; top: 396px;
    width: 566px; height: 270px;
    border-radius: 48px;
    border: 2px solid rgba(255,255,255,0.7);
    background:
      radial-gradient(ellipse at 50% 50%, var(--cloud) 0%, rgba(244,248,253,0.85) 40%, rgba(201,220,241,0.6) 100%),
      var(--cloud-edge);
    box-shadow: 0 0 40px rgba(255,255,255,0.45);
  }
  .info {
    position: absolute;
    left: 96px; top: 912px;
    font-size: 26px;
    line-height: 35px;
  }
  .info .venue { font-size: 32px; font-weight: 700; line-height: 40px; margin-bottom: 2px; }
  .info .spacer { display: inline-block; width: 24px; }
  .dates {
    position: absolute;
    left: 585px; top: 905px;
    width: 240px;
    text-align: center;
  }
  .dates .days { display: block; font-size: 96px; font-weight: 700; line-height: 0.95; letter-spacing: -3px; }
  .dates .month { display: block; font-size: 40px; font-weight: 400; line-height: 1.2; }
  .sponsors {
    position: absolute;
    left: 0; right: 0; top: 1093px;
    text-align: center;
    font-size: 36px;
    font-weight: 400;
  }
</style>
</head>
<body>
<main class="poster">
  <h1 class="title">
    <span class="title-small">Foire du</span>
    <span class="title-big">Rouet</span>
    <span class="subtitle">et de la mobilité durable</span>
  </h1>

  <div class="hero-visual" role="img" aria-label="Illustration d'un vélo dessiné en nuages blancs dans le ciel bleu"></div>

  <section class="info">
    <p class="venue">Halle RTP - Gare de Plantaz</p>
    <p>Ve 18 mars de 17h à 20h - Sa 19 mars</p>
    <p>de 10h à 18h - Di 20 mars de 10h à 17h</p>
    <p>Entrée gratuite<span class="spacer"></span>www.foire-du-rouet.ch</p>
  </section>

  <p class="dates">
    <span class="days">18-20</span>
    <span class="month">mars 2016</span>
  </p>

  <p class="sponsors">Sponsor Logo Here</p>
</main>
</body>
</html>
```